Business Cards

Business card design for my company.
I would like the card's background colour to be black. You can also see our web site to get an idea of our brand. https://www.dlqmarrowfield.com.au/
- Name
- Email

```html
<!DOCTYPE html>
<html lang="en">
<head>
<meta charset="utf-8">
<title>DLQ Marrowfield — Business Card</title>
<link rel="stylesheet" href="https://fonts.googleapis.com/css2?family=Arimo:wght@400;700&display=swap">
<style>
  :root {
    --page: #e4e4e4;
    --card: #2c2c2c;
    --green: #0a9444;
    --white: #f4f4f4;
    --text: #f0f0f0;
    --emboss: #3b3b3b;
  }
  html, body {
    margin: 0;
    width: 1200px;
    height: 1200px;
    overflow: hidden;
    background: var(--page);
    font-family: "Arimo", Arial, sans-serif;
  }
  .card {
    position: absolute;
    left: 256px;
    width: 688px;
    height: 393px;
    background: var(--card);
    color: var(--text);
  }
  .card--front { top: 160px; }
  .card--back { top: 650px; }

  .holder__name {
    position: absolute;
    left: 43px;
    top: 54px;
    margin: 0;
    font-size: 26px;
    font-weight: 700;
    color: var(--green);
    letter-spacing: 0.2px;
  }
  .holder__title {
    position: absolute;
    left: 43px;
    top: 88px;
    margin: 0;
    font-size: 15px;
  }
  .address {
    position: absolute;
    left: 44px;
    top: 196px;
    margin: 0;
    font-style: normal;
    font-size: 16px;
    line-height: 21px;
  }
  .contacts {
    position: absolute;
    left: 44px;
    top: 258px;
    margin: 0;
    padding: 0;
    list-style: none;
    font-size: 16px;
    line-height: 20.5px;
  }
  .contacts li {
    display: flex;
    align-items: center;
    gap: 10px;
  }
  .contacts svg {
    width: 14px;
    height: 14px;
    fill: var(--green);
    flex: none;
  }
  .brand {
    position: absolute;
    left: 315px;
    width: 340px;
    top: 170px;
    text-align: center;
    font-weight: 700;
    color: var(--white);
    line-height: 1;
    margin: 0;
  }
  .brand__main { display: block; font-size: 78px; letter-spacing: 4px; }
  .brand__sub { display: block; font-size: 24px; letter-spacing: 6px; margin-top: 12px; }

  .card--back .brand {
    left: 0;
    width: 688px;
    top: 140px;
    color: var(--emboss);
  }
</style>
</head>
<body>
  <section class="card card--front">
    <h1 class="holder__name">ALAN PEREIRA</h1>
    <p class="holder__title">President</p>

    <address class="address">412 Larkspur Road<br>Halden, Canada 58213</address>

    <ul class="contacts">
      <li>
        <svg viewBox="0 0 24 24" aria-hidden="true"><path d="M6.6 10.8a15.1 15.1 0 0 0 6.6 6.6l2.2-2.2c.3-.3.7-.4 1-.2 1.1.4 2.3.6 3.6.6.6 0 1 .4 1 1V20c0 .6-.4 1-1 1A17 17 0 0 1 3 4c0-.6.4-1 1-1h3.5c.6 0 1 .4 1 1 0 1.3.2 2.5.6 3.6.1.3 0 .7-.2 1z"/></svg>
        555-210-4816
      </li>
      <li>
        <svg viewBox="0 0 24 24" aria-hidden="true"><path d="M7 1h10a2 2 0 0 1 2 2v18a2 2 0 0 1-2 2H7a2 2 0 0 1-2-2V3a2 2 0 0 1 2-2zm0 3v15h10V4zm5 16.2a1 1 0 1 0 0 .1z"/></svg>
        555-372-9041
      </li>
      <li>
        <svg viewBox="0 0 24 24" aria-hidden="true"><path d="M2 5h20v14H2zm2 2v.5l8 5 8-5V7zm0 3v7h16v-7l-8 5z"/></svg>
        info@dlqmarrowfield.com
      </li>
      <li>
        <svg viewBox="0 0 24 24" aria-hidden="true"><path d="M12 2a10 10 0 1 0 0 20 10 10 0 0 0 0-20zm-1 17.9A8 8 0 0 1 4.2 10.6L9 15.4v1a2 2 0 0 0 2 2zm6.9-2.5A2 2 0 0 0 16 16h-1v-3a1 1 0 0 0-1-1H8v-2h2a1 1 0 0 0 1-1V7h2a2 2 0 0 0 2-2v-.4a8 8 0 0 1 2.9 12.8z"/></svg>
        www.dlqmarrowfield.com
      </li>
    </ul>

    <p class="brand">
      <span class="brand__main">DLQ</span>
      <span class="brand__sub">MARROWFIELD</span>
    </p>
  </section>

  <section class="card card--back">
    <p class="brand">
      <span class="brand__main">DLQ</span>
      <span class="brand__sub">MARROWFIELD</span>
    </p>
  </section>
</body>
</html>
```